Corporate Business Card

Very professional, Modern, Not to busy, include phone address email, website
(253) 555-0174, 61807 19th Street N, Kent, WA 98517, marcus@kestrelbayholding.com, brelvanindustries.com

Target Market(s)

Manufacturing

Industry/Entity Type

Aero, machining, manufacturing, Off road racing

Contact Information for Business Card

Phone, address email, website

```html
<!DOCTYPE html>
<html lang="en">
<head>
<meta charset="utf-8">
<title>Brelvan Industries – Business Card</title>
<link rel="stylesheet" href="https://fonts.googleapis.com/css2?family=Nunito+Sans:wght@600;700;800&display=swap">
<style>
  :root {
    --backdrop: #0a1844;
    --card-navy: #22346b;
    --card-navy-deep: #1b2b5c;
    --accent-red: #d9262b;
    --paper: #f2f2f4;
    --halftone-grey: #b9b9bd;
    --rule-navy: #1f3270;
    --white: #ffffff;
  }
  html, body {
    margin: 0;
    padding: 0;
    width: 1200px;
    height: 1160px;
    overflow: hidden;
    background: var(--backdrop);
    font-family: "Nunito Sans", Arial, sans-serif;
  }
  .canvas {
    position: relative;
    width: 1200px;
    height: 1160px;
  }
  .card {
    position: absolute;
    width: 509px;
    height: 291px;
    overflow: hidden;
  }
  /* Front */
  .card-front {
    left: 212px;
    top: 229px;
    background: var(--card-navy);
  }
  .front-texture {
    position: absolute;
    inset: 0 0 auto 0;
    height: 188px;
    background:
      radial-gradient(ellipse 70% 100% at 100% 0%, rgba(170, 24, 36, 0.75) 0%, rgba(120, 20, 50, 0.35) 45%, rgba(34, 52, 107, 0) 75%),
      radial-gradient(ellipse 55% 90% at 0% 0%, rgba(60, 80, 150, 0.55) 0%, rgba(34, 52, 107, 0) 70%);
  }
  .front-brand {
    position: absolute;
    left: 0;
    right: 0;
    top: 128px;
    display: flex;
    justify-content: center;
    align-items: center;
    gap: 12px;
  }
  .brand-mark {
    width: 14px;
    height: 14px;
    background: var(--accent-red);
  }
  .brand-name {
    font-weight: 800;
    font-size: 30px;
    letter-spacing: 0.5px;
    color: var(--white);
    line-height: 1;
  }
  /* Back */
  .card-back {
    left: 434px;
    top: 585px;
    background: var(--paper);
  }
  .back-texture {
    position: absolute;
    inset: 0 0 auto 0;
    height: 185px;
    background:
      radial-gradient(ellipse 30% 100% at 0% 0%, rgba(150, 150, 155, 0.75) 0%, rgba(242, 242, 244, 0) 80%),
      radial-gradient(ellipse 40% 100% at 100% 0%, rgba(150, 150, 155, 0.75) 0%, rgba(242, 242, 244, 0) 85%),
      linear-gradient(180deg, rgba(185, 185, 189, 0.55) 0%, rgba(242, 242, 244, 0) 100%);
  }
  .contact-rule {
    position: absolute;
    left: 43px;
    top: 129px;
    width: 6px;
    height: 137px;
    border-radius: 3px;
    background: var(--rule-navy);
  }
  .contact-list {
    position: absolute;
    left: 62px;
    top: 126px;
    margin: 0;
    padding: 0;
    list-style: none;
    font-weight: 700;
    font-size: 13.5px;
    line-height: 16.5px;
    color: var(--accent-red);
  }
  .contact-list .divider {
    height: 16.5px;
  }
  .contact-list .divider::before {
    content: "–";
  }
  .back-brand {
    position: absolute;
    right: 32px;
    bottom: 34px;
    display: flex;
    align-items: center;
    gap: 8px;
  }
  .back-brand .brand-mark {
    width: 9px;
    height: 9px;
  }
  .back-brand .brand-name {
    font-size: 19px;
    color: var(--rule-navy);
  }
</style>
</head>
<body>
<main class="canvas">
  <section class="card card-front" aria-label="Business card front">
    <div class="front-texture" role="img" aria-label="Halftone dot texture fading from blue at the left to red at the right"></div>
    <div class="front-brand">
      <span class="brand-mark"></span>
      <span class="brand-name">Brelvan Industries</span>
    </div>
  </section>

  <section class="card card-back" aria-label="Business card back">
    <div class="back-texture" role="img" aria-label="Grey halftone dot texture along the top edge"></div>
    <div class="contact-rule"></div>
    <ul class="contact-list">
      <li>253 555 0174</li>
      <li class="divider" aria-hidden="true"></li>
      <li>marcus@kestrelbayholding.com</li>
      <li class="divider" aria-hidden="true"></li>
      <li>61807 19th Street N,</li>
      <li>Kent, WA 98517</li>
      <li class="divider" aria-hidden="true"></li>
      <li>brelvanindustries.com</li>
    </ul>
    <div class="back-brand">
      <span class="brand-mark"></span>
      <span class="brand-name">Brelvan Industries</span>
    </div>
  </section>
</main>
</body>
</html>
```